Website Redesign for Mortgage, Property and Conveyancing business

Project Overview:
We are looking for a refresh and redesign of our current website to a smart, crisp and fresh approach to Home Loans, Conveyancing and Property sales. This task will be to:
- Redesign our current website in accordance with the new wireframe.
- Provide all elements required for the design
- Build 7 key templates including:
Home Page
2nd Level Section Page
3rd level Product landing Page
2nd Level - About Us, Contact Us etc
Blog
Blog Article
Campaign Page - no header
Technical
The design is for a Wordpress website. Existing theme is Quillnest and we use Elementor for page editing. We are open to a new theme to be introduced but would prefer to stay with elementor.
Current Site is: www.corvanta.com.au
Sites that we like or elements of sites:
Pelham Real Estate: https://www.pelham-example.com.au/ (Like use of video and navigation)
Copper Lantern Lane - Mortage: https://cll-example.com.au/refinance-home-loan/ (Like landing pages a sin example)
Marquetry: https://marquetry-example.com.au/ (like Our services section).
Industry/Entity Type
Mortgage, Property, Conveyancing, Property Investment
Coding
Coded - Design and coding required
Number of Pages Required
5+ page
Font styles to use
Requirements
Must have
- Built for Wordpress and Elementor.
Nice to have
- See Project Description for links to ideas/elements that we have liked. However, open to ideas as long as the follow the navigation set out in the wire frame.

```html
<!DOCTYPE html>
<html lang="en">
<head>
<meta charset="UTF-8">
<title>Brightwell Group – Finance, Property, Conveyancing</title>
<link href="https://fonts.googleapis.com/css2?family=Poppins:wght@400;600&family=Roboto:wght@400;500;700&display=swap" rel="stylesheet">
<style>
:root{
  --blue:#0b63b6;
  --navy:#0a4b8f;
  --deep:#07254d;
  --green:#17a34a;
  --ink:#2e3a4c;
  --muted:#5b6576;
  --soft:#eef2f6;
  --line:#d9dee6;
  --dots:#f1f3f6;
  --white:#ffffff;
}
*{box-sizing:border-box;margin:0;padding:0}
html,body{width:1200px;height:3019px;overflow:hidden}
body{position:relative;font-family:'Roboto',sans-serif;color:var(--ink);background:var(--white)}
.abs{position:absolute}

/* hero */
.hero{left:0;top:0;width:1200px;height:655px;background:linear-gradient(110deg,#2c4b78 0%,#1d3966 35%,#14305c 60%,#0c2245 100%)}
.brand{display:flex;align-items:center;gap:10px;font-family:'Roboto',sans-serif;font-weight:500;font-size:30px;color:var(--white)}
.brand-mark{width:30px;height:30px;background:var(--green)}
.hero-brand{left:111px;top:32px}
.menu{left:1060px;top:43px}
.hero-title{left:110px;top:148px;font-family:'Poppins',sans-serif;font-weight:600;font-size:53px;line-height:62px;color:var(--white)}
.hero-sub{left:110px;top:344px;font-family:'Poppins',sans-serif;font-size:26px;line-height:38px;color:var(--white)}
.btn{display:flex;align-items:center;justify-content:center;font-family:'Roboto',sans-serif;font-weight:500;font-size:18px;color:var(--white);text-decoration:none;border-radius:2px}
.btn-green{left:110px;top:448px;width:162px;height:47px;background:var(--green)}

/* services */
.eyebrow{font-size:19px;text-align:center;width:1200px;left:0}
.section-title{font-weight:500;font-size:42px;text-align:center;width:1200px;left:0;color:var(--ink)}
.dots{background:var(--dots)}
.card{width:311px;height:325px;border:2px solid var(--line);background:var(--white);text-align:center;padding-top:44px}
.card h3{font-weight:400;font-size:22px;margin-top:30px;color:#1c2430}
.card p{font-size:16.5px;line-height:24px;color:var(--muted);margin-top:8px}
.card.active{background:var(--blue);border-color:var(--blue)}
.card.active h3,.card.active p{color:var(--white)}

/* band */
.band{left:0;top:1236px;width:1088px;height:415px;border-radius:0 208px 208px 0;background:linear-gradient(100deg,#0a4d92 0%,#1159a4 45%,#0b4f97 100%)}
.band-eyebrow{left:112px;top:1302px;font-size:19px;color:#e2ebf6}
.band-title{left:112px;top:1326px;font-weight:500;font-size:33px;color:var(--white)}
.rule{width:42px;height:2px;background:var(--white)}
.band-col{width:340px;color:var(--white)}
.band-col h4{font-weight:700;font-size:22px}
.band-col p{font-size:16.5px;line-height:26px;margin-top:10px;color:#e7eef8}
.vline{width:1px;background:rgba(255,255,255,.4)}

/* outcome */
.outcome h2{font-weight:500;font-size:31px;line-height:39px;color:var(--ink)}
.outcome p{font-size:18px;line-height:30px;color:var(--muted);margin-top:14px}

/* news */
.news-bg{left:0;top:2036px;width:1200px;height:624px;background:var(--soft)}
.news-card{width:309px;height:352px;border-radius:3px;overflow:hidden}
.news-date{position:absolute;left:0;top:0;width:105px;height:37px;background:var(--blue);color:var(--white);font-size:12.5px;font-weight:500;display:flex;align-items:center;justify-content:center}
.news-caption{position:absolute;left:0;width:309px;top:264px;text-align:center;color:var(--white);font-weight:700;font-size:15.5px;line-height:25px;letter-spacing:-.3px}
.btn-blue{left:519px;top:2564px;width:162px;height:46px;background:var(--blue)}

/* footer */
.footer{left:0;top:2660px;width:1200px;height:359px;background:var(--navy)}
.footer-brand{left:94px;top:2793px;width:232px;height:76px;background:#c9d4e0;border-radius:4px;display:flex;align-items:center;justify-content:center;gap:10px;font-weight:500;font-size:26px;color:var(--navy)}
.footer-brand .brand-mark{width:26px;height:26px}
.fline{width:1px;background:rgba(255,255,255,.55);top:2704px;height:249px}
.fhead{font-weight:500;font-size:18px;color:var(--white)}
.links{list-style:none}
.links li{display:flex;align-items:center;gap:11px;font-size:15.5px;line-height:27.5px;color:#dce6f2}
.contact-item{display:flex;gap:20px;color:#dce6f2;font-size:15.5px;line-height:25px}
.contact-item svg{flex:none;margin-top:2px}
</style>
</head>
<body>

<!-- Hero -->
<div class="abs hero" role="img" aria-label="Photo of a hand using a laptop with glowing financial charts and figures"></div>
<div class="abs brand hero-brand"><span class="brand-mark"></span>Brightwell Group</div>
<svg class="abs menu" width="30" height="22" viewBox="0 0 30 22"><g stroke="#fff" stroke-width="2"><line x1="0" y1="3" x2="30" y2="3"/><line x1="0" y1="11" x2="30" y2="11"/><line x1="0" y1="19" x2="30" y2="19"/></g></svg>
<h1 class="abs hero-title">Finance<br>Property<br>Conveyancing</h1>
<p class="abs hero-sub">Unlocking Opportunities and<br>solving problems.</p>
<a class="abs btn btn-green" href="#">LEARN MORE</a>

<!-- Services -->
<p class="abs eyebrow" style="top:705px;color:var(--green)">What we do</p>
<h2 class="abs section-title" style="top:730px">Services We offer</h2>
<div class="abs dots" style="left:76px;top:769px;width:146px;height:136px" role="img" aria-label="Dot grid decoration"></div>
<div class="abs dots" style="left:988px;top:1040px;width:146px;height:136px" role="img" aria-label="Dot grid decoration"></div>

<div class="abs card active" style="left:112px;top:809px">
  <svg width="110" height="110" viewBox="0 0 110 110" fill="none" stroke="#fff" stroke-width="4" stroke-linecap="round" stroke-linejoin="round">
    <circle cx="55" cy="38" r="30"/><circle cx="55" cy="38" r="21"/>
    <path d="M61 29h-9a5 5 0 0 0 0 10h6a5 5 0 0 1 0 10h-10M55 24v5M55 49v5"/>
    <path d="M12 46v26l16 18v16M98 46v26l-16 18v16M12 60l14 16M98 60l-14 16"/>
  </svg>
  <h3>FINANCE</h3>
  <p>for your home, car<br>investments and assets</p>
</div>

<div class="abs card" style="left:444px;top:809px">
  <svg width="110" height="110" viewBox="0 0 110 110" fill="none" stroke-width="4" stroke-linecap="round" stroke-linejoin="round">
    <g stroke="#17a34a"><path d="M6 106h100M50 106V30h30v76M80 60h14v46M6 106V72l20-16 20 16v34"/><path d="M14 14v10M9 19h10M26 28v8M22 32h8"/></g>
    <g stroke="#0b63b6"><path d="M58 40h6M68 40h6M58 52h6M68 52h6M58 64h6M68 64h6M58 76h6M68 76h6M62 30v-10h6v10"/><path d="M30 80h-6a4 4 0 0 0 0 8h4a4 4 0 0 1 0 8h-6M26 76v4M26 96v4"/></g>
  </svg>
  <h3>PROPERTY</h3>
  <p>sales, purchases<br>and rentals</p>
</div>

<div class="abs card" style="left:776px;top:809px">
  <svg width="110" height="110" viewBox="0 0 110 110" fill="none" stroke-width="4" stroke-linecap="round" stroke-linejoin="round">
    <g stroke="#0b63b6"><circle cx="60" cy="32" r="28"/><path d="M48 26h24l-6-6M72 38H48l6 6"/></g>
    <g stroke="#17a34a"><path d="M8 70h14v34H8zM22 74h18c6 0 10 4 10 8H34M22 98l30 0 44-28c-4-6-10-6-16-2L58 82"/></g>
  </svg>
  <h3>CONVEYANCING</h3>
  <p>for seamless property<br>transactions</p>
</div>

<!-- Band -->
<div class="abs band" role="img" aria-label="Photo of a family at home under a blue overlay"></div>
<p class="abs band-eyebrow">What we do</p>
<h2 class="abs band-title">Services We offer</h2>
<div class="abs rule" style="left:112px;top:1390px"></div>
<div class="abs rule" style="left:574px;top:1390px"></div>
<div class="abs band-col" style="left:112px;top:1407px">
  <h4>20 years experience</h4>
  <p>We have grown and changed with the industry, and we’re dedicated to continually improve our service and products so you get the best solutions possible.</p>
</div>
<div class="abs vline" style="left:501px;top:1402px;height:152px"></div>
<div class="abs band-col" style="left:574px;top:1407px;width:360px">
  <h4>We give you choice</h4>
  <p>Working with over 20 large and small lenders, property developers and switched on account-ants, we have the scope to give you good choices for the future.</p>
</div>

<!-- Outcome -->
<div class="abs outcome" style="left:111px;top:1736px;width:400px">
  <h2>It is about the outcome</h2>
  <p>When we say we care, we mean it. If you are a client now, we want you to be a happy client. If we cannot help you become a client today we’d like to help you tomorrow.</p>
</div>
<div class="abs outcome" style="left:601px;top:1736px;width:400px">
  <h2>We give you options that<br>makes sense</h2>
  <p>Our team of finance, property investment and accounting experts know what they are talking about, and they are happy to take the time to explain things clearly.</p>
</div>

<!-- News -->
<div class="abs news-bg"></div>
<p class="abs eyebrow" style="top:2079px;color:var(--blue)">Latest</p>
<h2 class="abs section-title" style="top:2103px">News &amp; Articles</h2>

<div class="abs news-card" style="left:112px;top:2177px;background:linear-gradient(160deg,#6b6e73,#2d2f33 70%,#1d1e21)" role="img" aria-label="Photo of a hand touching floating property and finance icons">
  <span class="news-date">JUN 13, 2023</span>
  <p class="news-caption">Lorem Ipsum is simply dummy text<br>of the printing and typesetting</p>
</div>
<div class="abs news-card" style="left:445px;top:2177px;background:linear-gradient(170deg,#1e5d93,#0f3a6b 55%,#061b3a)" role="img" aria-label="Photo of hands holding a glowing house outline">
  <span class="news-date">JUN 13, 2023</span>
  <p class="news-caption">Lorem Ipsum is simply dummy text<br>of the printing and typesetting</p>
</div>
<div class="abs news-card" style="left:780px;top:2177px;background:linear-gradient(160deg,#b7ac9c,#7b6b5e 55%,#3e3631)" role="img" aria-label="Photo of a smiling couple reviewing documents">
  <span class="news-date">JUN 13, 2023</span>
  <p class="news-caption">Lorem Ipsum is simply dummy text<br>of the printing and typesetting</p>
</div>
<a class="abs btn btn-blue" href="#">READ MORE</a>

<!-- Footer -->
<div class="abs footer"></div>
<div class="abs footer-brand"><span class="brand-mark"></span>Brightwell Group</div>
<div class="abs fline" style="left:372px"></div>
<div class="abs fline" style="left:753px"></div>

<h3 class="abs fhead" style="left:458px;top:2729px">LINKS</h3>
<ul class="abs links" style="left:458px;top:2771px">
  <li><svg width="14" height="14" viewBox="0 0 14 14"><circle cx="7" cy="7" r="7" fill="#c9d4e0"/><path d="M6 4l3 3-3 3" stroke="#0a4b8f" stroke-width="1.6" fill="none"/></svg>Finance</li>
  <li><svg width="14" height="14" viewBox="0 0 14 14"><circle cx="7" cy="7" r="7" fill="#c9d4e0"/><path d="M6 4l3 3-3 3" stroke="#0a4b8f" stroke-width="1.6" fill="none"/></svg>Property Investment</li>
  <li><svg width="14" height="14" viewBox="0 0 14 14"><circle cx="7" cy="7" r="7" fill="#c9d4e0"/><path d="M6 4l3 3-3 3" stroke="#0a4b8f" stroke-width="1.6" fill="none"/></svg>Property Purchase &amp; Sales</li>
  <li><svg width="14" height="14" viewBox="0 0 14 14"><circle cx="7" cy="7" r="7" fill="#c9d4e0"/><path d="M6 4l3 3-3 3" stroke="#0a4b8f" stroke-width="1.6" fill="none"/></svg>Property Management</li>
  <li><svg width="14" height="14" viewBox="0 0 14 14"><circle cx="7" cy="7" r="7" fill="#c9d4e0"/><path d="M6 4l3 3-3 3" stroke="#0a4b8f" stroke-width="1.6" fill="none"/></svg>Conveyancing</li>
  <li><svg width="14" height="14" viewBox="0 0 14 14"><circle cx="7" cy="7" r="7" fill="#c9d4e0"/><path d="M6 4l3 3-3 3" stroke="#0a4b8f" stroke-width="1.6" fill="none"/></svg>About</li>
  <li><svg width="14" height="14" viewBox="0 0 14 14"><circle cx="7" cy="7" r="7" fill="#c9d4e0"/><path d="M6 4l3 3-3 3" stroke="#0a4b8f" stroke-width="1.6" fill="none"/></svg>Contact</li>
</ul>

<h3 class="abs fhead" style="left:845px;top:2729px">CONTACT</h3>
<div class="abs contact-item" style="left:852px;top:2773px">
  <svg width="20" height="24" viewBox="0 0 20 24"><path d="M10 0a9 9 0 0 0-9 9c0 7 9 15 9 15s9-8 9-15a9 9 0 0 0-9-9z" fill="#c9d4e0"/><circle cx="10" cy="9" r="3.5" fill="#0a4b8f"/></svg>
  <div>Address<br>418 Meridian Ave.</div>
</div>
<div class="abs contact-item" style="left:852px;top:2838px">
  <svg width="20" height="20" viewBox="0 0 24 24"><path d="M6.6 10.8a15 15 0 0 0 6.6 6.6l2.2-2.2a1 1 0 0 1 1-.25 11 11 0 0 0 3.6.6 1 1 0 0 1 1 1V20a1 1 0 0 1-1 1A17 17 0 0 1 3 4a1 1 0 0 1 1-1h3.5a1 1 0 0 1 1 1 11 11 0 0 0 .6 3.6 1 1 0 0 1-.25 1z" fill="#c9d4e0"/></svg>
  <div>Phone:<br>1300 418 270</div>
</div>
<div class="abs contact-item" style="left:852px;top:2900px">
  <svg width="22" height="18" viewBox="0 0 22 18"><rect x="0" y="1" width="22" height="16" rx="2" fill="#c9d4e0"/><path d="M1 3l10 7 10-7" stroke="#0a4b8f" stroke-width="1.8" fill="none"/></svg>
  <div>Email:<br>hello@brightwellgroup.com</div>
</div>

</body>
</html>
```